Maple Hollow Bloom Backdrops Business card

Looking to have a business card design incorporating my logo for my flower wall business.

Industry/Entity Type

Wedding & event planning

Contact Information for Business Card

My business logo, my name - Jill Worthing (owner), my tagline - petals for every lovely moment, phone # 401-627-3918, email address - maplehollowbloombackdrops@fernpost.com, my website - maplehollowbloombackdrops.com, Instagram handle- @maplehollowbloombackdrops, FB handle Handle - maplehollowbloombackdrops

Font styles to use
Other font styles liked:
• Sentaina is the font that is used in my logo

Requirements
Must have
• Would like a double sided business card

```html
<!DOCTYPE html>
<html lang="en">
<head>
<meta charset="utf-8">
<title>Maple Hollow Bloom Backdrops — Business Card</title>
<link rel="stylesheet" href="https://fonts.googleapis.com/css2?family=Libre+Baskerville:ital,wght@0,400;1,400&family=Sacramento&display=swap">
<style>
  :root {
    --backdrop: #ead3d6;
    --card-white: #ffffff;
    --card-pink: #f07da2;
    --pattern-pink: #f59bb8;
    --accent-pink: #e2558a;
    --frame-pink: #e7769e;
    --ink: #2a2a2a;
    --soft-leaf: #f8e4ea;
  }
  * { box-sizing: border-box; margin: 0; padding: 0; }
  html, body { width: 1200px; height: 1000px; overflow: hidden; }
  body {
    background: var(--backdrop);
    display: flex;
    align-items: center;
    justify-content: center;
    gap: 40px;
  }
  .card {
    position: relative;
    width: 520px;
    height: 297px;
    overflow: hidden;
  }

  /* Back side */
  .card--back { background: var(--card-pink); }
  .leaf-pattern {
    position: absolute; inset: 0;
    background: radial-gradient(circle at 30% 40%, var(--pattern-pink) 0%, var(--card-pink) 70%);
    opacity: .7;
  }
  .logo-badge {
    position: absolute;
    left: 50%; top: 50%;
    width: 160px; height: 160px;
    transform: translate(-50%, -50%);
    border-radius: 50%;
    background: var(--card-white);
    display: flex; align-items: center; justify-content: center;
    text-align: center;
    padding: 22px;
  }
  .logo-badge__name {
    font-family: "Libre Baskerville", serif;
    font-size: 15px;
    line-height: 1.35;
    color: var(--ink);
  }

  /* Front side */
  .card--front { background: var(--card-white); }
  .corner-sprig {
    position: absolute;
    top: 14px;
    width: 90px; height: 56px;
    background: radial-gradient(ellipse at center, var(--soft-leaf) 0%, rgba(248,228,234,0) 70%);
  }
  .corner-sprig--left { left: 8px; }
  .corner-sprig--right { right: 8px; }
  .brand-name {
    position: absolute;
    top: 34px; left: 0; right: 0;
    text-align: center;
    font-family: "Libre Baskerville", serif;
    font-size: 19px;
    color: var(--ink);
  }
  .info-frame {
    position: absolute;
    left: 24px; right: 24px;
    top: 104px; bottom: 20px;
    border: 1.5px solid var(--frame-pink);
  }
  .tagline {
    position: absolute;
    top: -9px; left: 50%;
    transform: translateX(-50%);
    background: var(--card-white);
    padding: 0 10px;
    white-space: nowrap;
    font-family: "Libre Baskerville", serif;
    font-style: italic;
    font-size: 11px;
    letter-spacing: 1.6px;
    color: var(--accent-pink);
  }
  .owner-name {
    position: absolute;
    top: 6px; left: 0; right: 0;
    text-align: center;
    font-family: "Sacramento", cursive;
    font-size: 50px;
    color: var(--accent-pink);
  }
  .contact {
    position: absolute;
    left: 0; right: 0; bottom: 0;
    height: 74px;
    border-top: 1.5px solid var(--frame-pink);
    display: flex; flex-direction: column;
    align-items: center; justify-content: center;
    gap: 9px;
    font-family: "Libre Baskerville", serif;
    font-size: 11px;
    color: var(--ink);
    letter-spacing: .3px;
  }
  .contact__line { display: flex; align-items: center; gap: 6px; white-space: nowrap; }
  .contact__dot {
    width: 11px; height: 11px;
    border-radius: 50%;
    background: var(--accent-pink);
  }
</style>
</head>
<body>

  <section class="card card--back" aria-label="Business card back">
    <div class="leaf-pattern" role="img" aria-label="Repeating light pink leaf and berry pattern"></div>
    <div class="logo-badge">
      <span class="logo-badge__name">Maple Hollow Bloom Backdrops</span>
    </div>
  </section>

  <section class="card card--front" aria-label="Business card front">
    <div class="corner-sprig corner-sprig--left" role="img" aria-label="Faint pink leaf sprig decoration"></div>
    <div class="corner-sprig corner-sprig--right" role="img" aria-label="Faint pink leaf sprig decoration"></div>
    <p class="brand-name">Maple Hollow Bloom Backdrops</p>
    <div class="info-frame">
      <p class="tagline">petals for every lovely moment</p>
      <p class="owner-name">Jill Worthing</p>
      <div class="contact">
        <p class="contact__line">401-627-3918 | maplehollowbloombackdrops@fernpost.com</p>
        <p class="contact__line">maplehollowbloombackdrops.com | <span class="contact__dot"></span> maplehollowbloombackdrops</p>
      </div>
    </div>
  </section>

</body>
</html>
```